Remote Billing Advertisement Needed - Medical/Healthcare

Trovel Capital, Inc. is a receivables management solutions firm dedicated to the surgical industry. Our clients are large medical management companies who own and operate surgical hospitals and surgery centers nationwide. We have added an additional line of business to our repertoire and are looking to design an advertisement that will highlight the benefits of the service to our target audience.

See attached creative brief for additional information.

Target Market(s)

Busy medical office managers (but should still have value to a C-level viewer)

Industry/Entity Type

Medical

Font styles to use
Serif

Requirements
Must have
• A contemporary design and a conversational tone
• Trovel Capital's logo

```html
<!DOCTYPE html>
<html lang="en">
<head>
<meta charset="utf-8">
<title>Reclaim Your Patient AR – Trovel Capital</title>
<link rel="stylesheet" href="https://fonts.googleapis.com/css2?family=Roboto:ital,wght@0,300;0,400;0,700;0,900;1,700;1,900&family=Roboto+Condensed:wght@700&family=Comic+Neue:wght@700&display=swap">
<style>
  :root {
    --navy: #0d0d33;
    --maroon: #4a0c0c;
    --grey: #6b6c70;
    --ink: #111111;
    --text-grey: #58595b;
    --pale-blue: #b7d3ec;
    --white: #ffffff;
    --photo-light: #f2f2f2;
    --photo-mid: #c9ccd2;
  }
  * { box-sizing: border-box; margin: 0; padding: 0; }
  html, body { width: 848px; height: 1200px; overflow: hidden; background: var(--white); }
  body { font-family: "Roboto", Arial, sans-serif; color: var(--ink); }
  .ad { position: relative; width: 848px; height: 1200px; }
  .abs { position: absolute; }

  .header-band { left: 0; top: 0; width: 848px; height: 170px; }
  .headline {
    left: 0; top: 38px; width: 848px; text-align: center;
    font: italic 900 56px/1 "Roboto", Arial, sans-serif; color: var(--white); letter-spacing: 0.5px;
  }
  .tagline {
    left: 0; top: 143px; width: 848px; text-align: center;
    font: 400 19px/1 "Roboto", Arial, sans-serif; color: var(--ink); letter-spacing: 0.5px;
  }

  .offer { width: 236px; height: 106px; }
  .offer-text {
    position: absolute; left: 0; top: 8px; width: 236px; text-align: center;
    font: italic 900 18px/1.15 "Roboto", Arial, sans-serif; color: var(--white);
  }
  .offer--calls-out { left: 52px; top: 192px; }
  .offer--calls-in { left: 308px; top: 192px; }
  .offer--agreements { left: 566px; top: 192px; }

  .lead {
    left: 0; top: 306px; width: 848px; text-align: center;
    font: 300 42px/1 "Roboto", Arial, sans-serif; color: var(--text-grey);
  }
  .lead .lead-and { color: var(--navy); }
  .lead .lead-ready { color: var(--maroon); }

  .photo {
    left: 52px; top: 366px; width: 746px; height: 404px;
    background: radial-gradient(ellipse at 50% 55%, var(--photo-mid) 0%, var(--photo-light) 60%, var(--white) 100%);
  }
  .bubble { width: 280px; height: 180px; }
  .bubble-text {
    position: absolute; left: 0; width: 280px; text-align: center;
    font: 700 21px/1.35 "Comic Neue", "Comic Sans MS", cursive;
  }
  .bubble--notes { left: 58px; top: 376px; }
  .bubble--notes .bubble-text { top: 48px; color: var(--maroon); }
  .bubble--time { left: 548px; top: 382px; }
  .bubble--time .bubble-text { top: 30px; color: var(--navy); }

  .how-panel {
    left: 52px; top: 786px; width: 746px; height: 246px;
    background: var(--navy); border-radius: 0 0 22px 22px;
  }
  .how-title {
    left: 286px; top: 796px; width: 276px; height: 30px; border-radius: 6px;
    background: var(--pale-blue); text-align: center;
    font: 900 20px/30px "Roboto", Arial, sans-serif; color: var(--navy);
  }
  .step-tab {
    top: 830px; width: 134px; height: 36px; border-radius: 10px 10px 0 0;
    background: var(--navy); border: 2px solid var(--white); border-bottom: none;
    text-align: center; font: 900 21px/34px "Roboto Condensed", Arial, sans-serif; color: var(--white);
  }
  .step-tab--one { left: 36px; }
  .step-tab--two { left: 682px; }
  .steps-row { left: 52px; top: 862px; width: 746px; height: 80px; }
  .step-one-text {
    left: 52px; top: 880px; width: 120px; text-align: center;
    font: 400 15px/1.3 "Roboto", Arial, sans-serif; color: var(--ink);
  }
  .step-two-text {
    left: 196px; top: 880px; width: 596px; text-align: center;
    font: 400 15px/1.3 "Roboto", Arial, sans-serif; color: var(--ink);
  }
  .panel-statement {
    left: 52px; top: 956px; width: 746px; text-align: center;
    font: italic 700 17px/1.3 "Roboto", Arial, sans-serif; color: var(--white);
  }
  .service {
    top: 1018px; height: 50px; border: 2px solid var(--white); border-radius: 12px;
    background: var(--navy); text-align: center;
    font: italic 900 16px/46px "Roboto", Arial, sans-serif; color: var(--white);
  }
  .service--payplan { left: 62px; width: 274px; }
  .service--precollect { left: 348px; width: 212px; }
  .service--baddebt { left: 572px; width: 216px; }

  .phone {
    left: 50px; top: 1088px;
    font: 700 54px/1 "Roboto Condensed", Arial, sans-serif; color: var(--ink); letter-spacing: -1px;
  }
  .web {
    left: 52px; top: 1139px;
    font: 700 19px/1 "Roboto", Arial, sans-serif; color: var(--maroon);
  }
  .brand { left: 396px; top: 1098px; display: flex; align-items: center; gap: 10px; }
  .brand-square { width: 22px; height: 22px; background: var(--maroon); }
  .brand-name { font: 700 30px/1 "Roboto", Arial, sans-serif; color: var(--text-grey); }
  .brand-rule { left: 668px; top: 1090px; width: 1px; height: 76px; background: var(--text-grey); }
  .descriptor {
    left: 680px; top: 1096px;
    font: 400 17px/1.3 "Roboto", Arial, sans-serif; color: var(--maroon);
  }
</style>
</head>
<body>
<main class="ad">
  <svg class="abs header-band" viewBox="0 0 848 170" aria-hidden="true">
    <rect x="0" y="0" width="848" height="132" fill="var(--navy)"/>
    <polygon points="0,132 92,132 0,168" fill="var(--navy)"/>
    <polygon points="848,132 756,132 848,168" fill="var(--navy)"/>
  </svg>
  <h1 class="abs headline">RECLAIM YOUR PATIENT AR</h1>
  <p class="abs tagline">NOT JUST ANOTHER LETTER SERIES!</p>

  <div class="abs offer offer--calls-out">
    <svg width="236" height="106" aria-hidden="true"><path d="M12 0h212a12 12 0 0 1 12 12v54a12 12 0 0 1-12 12H138l-20 26-20-26H12A12 12 0 0 1 0 66V12A12 12 0 0 1 12 0z" fill="var(--grey)"/></svg>
    <p class="offer-text">LET US<br>make the<br>telephone calls</p>
  </div>
  <div class="abs offer offer--calls-in">
    <svg width="236" height="106" aria-hidden="true"><path d="M12 0h212a12 12 0 0 1 12 12v54a12 12 0 0 1-12 12H138l-20 26-20-26H12A12 12 0 0 1 0 66V12A12 12 0 0 1 12 0z" fill="var(--navy)"/></svg>
    <p class="offer-text">LET US<br>answer the<br>telephone calls</p>
  </div>
  <div class="abs offer offer--agreements">
    <svg width="236" height="106" aria-hidden="true"><path d="M12 0h212a12 12 0 0 1 12 12v54a12 12 0 0 1-12 12H138l-20 26-20-26H12A12 12 0 0 1 0 66V12A12 12 0 0 1 12 0z" fill="var(--maroon)"/></svg>
    <p class="offer-text">LET US<br>establish payment<br>agreements</p>
  </div>

  <p class="abs lead">Let us accept payments, <span class="lead-and">and…</span> <span class="lead-ready">ready?</span></p>

  <div class="abs photo" role="img" aria-label="Photo of a smiling businesswoman in a grey suit with open palms, presenting the service"></div>

  <div class="abs bubble bubble--notes">
    <svg width="280" height="180" aria-hidden="true"><ellipse cx="136" cy="80" rx="130" ry="76" fill="var(--white)" stroke="#555" stroke-width="1.5" stroke-dasharray="2 3"/><path d="M200 142 L262 176 L222 136" fill="var(--white)" stroke="#555" stroke-width="1.5" stroke-dasharray="2 3"/></svg>
    <p class="bubble-text">Make notes<br>directly into you’re<br>HIS</p>
  </div>
  <div class="abs bubble bubble--time">
    <svg width="280" height="180" aria-hidden="true"><ellipse cx="142" cy="86" rx="134" ry="84" fill="var(--white)" stroke="#555" stroke-width="1.5" stroke-dasharray="2 3"/><path d="M60 148 L0 178 L42 140" fill="var(--white)" stroke="#555" stroke-width="1.5" stroke-dasharray="2 3"/></svg>
    <p class="bubble-text">Imagine the extra<br>time your team will<br>have to work the<br>insurance claims</p>
  </div>

  <div class="abs how-panel"></div>
  <h2 class="abs how-title">HOW IT WORKS</h2>
  <svg class="abs steps-row" viewBox="0 0 746 80" aria-hidden="true">
    <rect x="0" y="0" width="130" height="80" fill="var(--white)"/>
    <polygon points="130,0 146,0 146,80 130,80 130,56 144,40 130,24" fill="var(--navy)"/>
    <rect x="146" y="0" width="600" height="80" fill="var(--white)"/>
    <polygon points="694,80 730,80 712,96" fill="var(--white)"/>
  </svg>
  <div class="abs step-tab step-tab--one">STEP 1</div>
  <div class="abs step-tab step-tab--two">STEP 2</div>
  <p class="abs step-one-text">You set the<br>parameters.</p>
  <p class="abs step-two-text">We utilize a combination of call center agents and remote billing support we login into your billing system each day and work your accounts as if we were sitting in the office next to you.</p>
  <p class="abs panel-statement">By strategically placing remote billing agents throughout the U.S.,<br>we help you to maximize your efficiencies and reduce your cost by establishing:</p>
  <div class="abs service service--payplan">PAY-PLAN MANAGEMENT</div>
  <div class="abs service service--precollect">PRE-COLLECTIONS</div>
  <div class="abs service service--baddebt">BAD DEBT</div>

  <p class="abs phone">800.555.0147</p>
  <p class="abs web">www.trovelcapital.com</p>
  <div class="abs brand"><span class="brand-square"></span><span class="brand-name">Trovel Capital</span></div>
  <div class="abs brand-rule"></div>
  <p class="abs descriptor">Receivable<br>Management<br>Solutions</p>
</main>
</body>
</html>
```